Business Card Design

We are a florist shop that also stocks a range of giftware and jewellery. I would like a new design that incorporates a light green background. If you could use a skeleton leaf somewhere in the design that would be great. I would also like to incorporate the find us on Friendloop logo on this design.

Industry/Entity Type

Florist

Contact Information for Business Card

Petals on Harwick
42 Tennant street
Brellan Vale 3915
Phone: 0351938426
Fax : 0351938470
email: poh@lakemail.net.au

Proprietors : Dana & Lee Morcombe

```html
<!DOCTYPE html>
<html lang="en">
<head>
<meta charset="utf-8">
<title>Petals on Harwick – Business Card</title>
<link rel="stylesheet" href="https://fonts.googleapis.com/css2?family=Cormorant+Garamond:wght@500&family=Open+Sans:wght@400;600&display=swap">
<style>
  :root {
    --page: #ffffff;
    --leaf-deep: #3f8a3c;
    --leaf-mid: #6fb24a;
    --leaf-lime: #a9d340;
    --leaf-pale: #d6ecc4;
    --band: #2f7a33;
    --ink-light: #ffffff;
    --shadow: rgba(0, 0, 0, 0.35);
  }
  * { box-sizing: border-box; margin: 0; padding: 0; }
  html, body { width: 1200px; height: 900px; overflow: hidden; background: var(--page); }
  .canvas { position: relative; width: 1200px; height: 900px; }

  .card { position: absolute; overflow: hidden; box-shadow: 3px 4px 6px var(--shadow); }
  .card--front { left: 60px; top: 250px; width: 660px; height: 370px; }
  .card--back { left: 755px; top: 0; width: 445px; height: 268px; box-shadow: none; }

  .card__photo {
    position: absolute; inset: 0;
    background:
      radial-gradient(ellipse 40% 30% at 25% 20%, rgba(230,245,220,0.8), transparent 70%),
      radial-gradient(ellipse 50% 35% at 65% 55%, var(--leaf-lime), transparent 75%),
      radial-gradient(ellipse 45% 40% at 60% 95%, var(--leaf-pale), transparent 70%),
      linear-gradient(160deg, var(--leaf-mid) 0%, var(--leaf-deep) 45%, var(--leaf-lime) 75%, var(--leaf-pale) 100%);
  }
  .card__bands { position: absolute; inset: 0; width: 100%; height: 100%; }

  .brand {
    position: absolute; color: var(--ink-light);
    font-family: "Cormorant Garamond", serif; font-weight: 500; font-style: normal;
    line-height: 1; white-space: nowrap;
  }
  .card--front .brand { left: 108px; top: 160px; font-size: 58px; }
  .card--back .brand { left: 232px; top: 118px; font-size: 26px; }

  .contact {
    position: absolute; right: 232px; top: 98px; text-align: right; font-style: normal;
    color: var(--ink-light); font-family: "Open Sans", sans-serif; font-size: 12px; line-height: 16.5px;
  }
  .divider { position: absolute; left: 223px; top: 74px; width: 1px; height: 118px; background: var(--ink-light); opacity: 0.8; }
  .address {
    position: absolute; right: 16px; top: 228px; font-style: normal;
    color: var(--ink-light); font-family: "Open Sans", sans-serif; font-weight: 600; font-size: 11px;
  }
</style>
</head>
<body>
<main class="canvas">

  <section class="card card--front" aria-label="Business card front">
    <div class="card__photo" role="img" aria-label="Soft-focus macro photograph of a pale green flower"></div>
    <svg class="card__bands" viewBox="0 0 660 370" preserveAspectRatio="none" aria-hidden="true">
      <polygon points="300,0 660,0 660,290" fill="var(--band)" opacity="0.35"/>
      <polygon points="360,0 660,0 660,240" fill="var(--band)" opacity="0.4"/>
      <polygon points="430,0 660,0 660,185" fill="var(--band)" opacity="0.45"/>
      <polygon points="505,0 660,0 660,125" fill="var(--band)" opacity="0.5"/>
      <polygon points="0,130 0,370 185,370" fill="var(--band)" opacity="0.35"/>
      <polygon points="0,190 0,370 140,370" fill="var(--band)" opacity="0.4"/>
      <polygon points="0,250 0,370 95,370" fill="var(--band)" opacity="0.45"/>
    </svg>
    <h1 class="brand">Petals on Harwick</h1>
  </section>

  <section class="card card--back" aria-label="Business card back">
    <div class="card__photo" role="img" aria-label="Soft-focus macro photograph of a pale green flower"></div>
    <svg class="card__bands" viewBox="0 0 445 268" preserveAspectRatio="none" aria-hidden="true">
      <polygon points="0,70 0,268 125,268" fill="var(--band)" opacity="0.35"/>
      <polygon points="0,115 0,268 95,268" fill="var(--band)" opacity="0.4"/>
      <polygon points="0,165 0,268 62,268" fill="var(--band)" opacity="0.45"/>
    </svg>
    <address class="contact">
      Phone: 0351938426<br>
      Fax : 0351938470<br>
      email:poh@lakemail.net.au<br>
      P 0351-938-400
    </address>
    <div class="divider"></div>
    <h2 class="brand">Petals on Harwick</h2>
    <p class="address">42 Tennant street Brellan Vale 3915</p>
  </section>

</main>
</body>
</html>
```